Airshow Company & Product A4 Double sided Flyer Template

Design an A4 Double sided template that our three company divisions can use for an airshow in February. 3 Divisional businesses (TRONVEX, PALEDORN, KUBLINOR) Aviation feel for the flyer. Our flyer will include front parts, Introduction (Company introduction) Brands offered (logos) then on the back of the A4 page, full colour products or product shown. Document needs to be in a format we can replace the text, logo and pictures for each company division as required.

Target Market(s)

Aviation

Industry/Entity Type

Aviation

Font styles to use
Sans Serif

Requirements
Must have
• Clear template for use by three divisions. Same design used by three divisions with different logos, images etc

```html
<!DOCTYPE html>
<html lang="en">
<head>
<meta charset="utf-8">
<title>Paledorn Airshow Flyer</title>
<link rel="stylesheet" href="https://fonts.googleapis.com/css2?family=Raleway:wght@400;500;600;700;800&display=swap">
<style>
  :root{
    --blue:#0b6fc2;
    --blue-soft:#4e8fd0;
    --ink:#3a3a3a;
    --text:#555;
    --grey:#d9d9d9;
    --grey-light:#eeeeee;
    --panel:#e4e9f6;
    --stage:#2e2e2e;
    --white:#ffffff;
  }
  *{box-sizing:border-box;margin:0;padding:0}
  html,body{width:1200px;height:1200px;overflow:hidden;background:var(--stage)}
  body{font-family:"Raleway",sans-serif;color:var(--text);position:relative}
  .page{position:absolute;top:208px;width:536px;height:758px;background:var(--white);overflow:hidden}
  .page--front{left:57px}
  .page--back{left:602px}
  .abs{position:absolute}
  .brand{display:flex;align-items:center;gap:8px;font-weight:500;color:var(--blue);letter-spacing:1px}
  .brand__dot{width:22px;height:22px;border-radius:50%;background:var(--blue)}
  .headline{left:0;width:536px;top:334px;text-align:center;font-size:36px;font-weight:500;color:var(--ink);letter-spacing:-0.5px}
  .headline b{color:var(--blue);font-weight:800}
  .subhead{left:0;width:536px;top:372px;text-align:center;font-size:22px;font-weight:800;color:var(--ink);letter-spacing:-0.5px}
  .body-copy{left:22px;width:494px;font-size:10.4px;line-height:14.4px;color:var(--text)}
  .offers-tab{left:155px;top:506px;width:226px;height:24px}
  .offers-tab span{position:absolute;left:0;width:226px;top:3px;text-align:center;color:var(--white);font-weight:600;font-size:16px}
  .offers{left:0;top:528px;width:536px;height:162px;display:flex}
  .offer{height:100%;position:relative;text-align:center}
  .offer--a{width:174px;background:var(--grey)}
  .offer--b{width:187px;background:var(--grey-light)}
  .offer--c{width:175px;background:var(--grey)}
  .offer__logo{width:80px;height:80px;border-radius:50%;background:var(--white);margin:8px auto 0;display:flex;align-items:center;justify-content:center;color:var(--blue);font-weight:700;font-size:22px}
  .offer__text{font-size:7.6px;line-height:9.6px;color:var(--text);margin:22px auto 0;width:138px}
  .footer{left:0;top:690px;width:536px;height:68px;display:flex;color:var(--white)}
  .footer__col{height:100%;position:relative}
  .footer__col--left{width:174px;background:var(--blue-soft);padding:14px 0 0 22px;font-size:8.5px;line-height:12px}
  .footer__col--mid{width:187px;background:var(--blue);padding:6px 0 0 0;text-align:center}
  .footer__col--right{width:175px;background:var(--blue-soft);padding:7px 0 0 54px;font-size:8.2px;line-height:14.5px}
  .footer strong{font-weight:700;font-size:10px}
  .ph-big{font-weight:700;font-size:13.5px;line-height:14px}
  .ph-small{font-size:8px;margin-top:4px}
  .title{left:0;width:536px;top:172px;text-align:center;font-size:40px;font-weight:500;color:var(--ink);letter-spacing:-0.5px}
  .title b{color:var(--blue);font-weight:800}
  .intro{left:40px;width:456px;top:219px;text-align:center;font-size:11px;line-height:14.5px;color:var(--ink)}
  .card{left:22px;width:492px;height:179px;background:var(--panel);border-radius:0 12px 12px 0}
  .card__photo{position:absolute;left:0;top:0;width:190px;height:179px}
  .card__tab{position:absolute;left:222px;top:0;width:230px;height:26px}
  .card__tab span{position:absolute;left:0;width:230px;top:5px;text-align:center;color:var(--blue);font-weight:700;font-size:15.5px}
  .spec{position:absolute;left:215px;width:270px;font-size:8.2px;color:var(--ink)}
  .spec__label{position:absolute;left:0;font-weight:700;font-size:10px}
  .spec__value{position:absolute;left:84px;line-height:12.6px}
  .spec__rule{position:absolute;left:0;width:270px;height:1px;background:#a9bfe6}
  .contact{left:22px;top:668px;color:var(--blue)}
  .contact__num{position:absolute;left:46px;top:0;font-weight:700;font-size:19px;line-height:20px;white-space:nowrap}
  .contact__hours{position:absolute;left:0;top:46px;font-size:11px;color:var(--text);white-space:nowrap}
</style>
</head>
<body>

<section class="page page--front">
  <svg class="abs" style="left:0;top:0" width="536" height="330" viewBox="0 0 536 330">
    <defs>
      <linearGradient id="skyFront" x1="0" y1="0" x2="0" y2="1">
        <stop offset="0" stop-color="#5e85ad"/>
        <stop offset="0.5" stop-color="#dfe4ea"/>
        <stop offset="1" stop-color="#b6b9bd"/>
      </linearGradient>
    </defs>
    <rect width="536" height="330" fill="url(#skyFront)" role="img" aria-label="Photo of a private jet parked on the apron with stairs down"/>
    <path d="M130 0 Q300 130 536 130 L536 0 Z" fill="#fff"/>
    <path d="M0 270 Q250 330 536 236 L536 330 L0 330 Z" fill="var(--blue)"/>
    <path d="M0 296 Q270 340 536 248 L536 330 L0 330 Z" fill="#fff"/>
  </svg>
  <div class="abs brand" style="left:330px;top:54px;font-size:28px"><span class="brand__dot"></span>PALEDORN</div>

  <h1 class="abs headline"><b>YOUR</b> HEAD WILL <b>GO HERE</b></h1>
  <h2 class="abs subhead">..YOUR SUBHEAD WILL GO HERE</h2>
  <p class="abs body-copy" style="top:404px">As we own and maintain our own fleet of executive jets and other aircraft, we are able to guarantee the highest level of safety, security and satisfaction. Nothing is too much to ask of us - we'll go the extra mile to ensure your flight meets your expectations. We provide our clients with a completely stress free and relaxing private jet travel experience.</p>
  <p class="abs body-copy" style="top:467px">Our exclusive clientele continue their patronage whenever they need to travel in complete privacy, comfort and style due to our culture of outstanding customer service and attention to detail.</p>

  <div class="abs offers">
    <div class="offer offer--a"><div class="offer__logo">LOGO</div><p class="offer__text">Paledorn is Australia's premier jet charter company providing executive jet hire for Australian clients and companies.</p></div>
    <div class="offer offer--b"><div class="offer__logo">LOGO</div><p class="offer__text">Paledorn is Australia's premier jet charter company providing executive jet hire for Australian clients and companies.</p></div>
    <div class="offer offer--c"><div class="offer__logo">LOGO</div><p class="offer__text">Paledorn is Australia's premier jet charter company providing executive jet hire for Australian clients and companies.</p></div>
  </div>
  <div class="abs offers-tab">
    <svg width="226" height="24" viewBox="0 0 226 24"><path d="M0 24 Q10 0 30 0 L196 0 Q216 0 226 24 Z" fill="var(--blue)"/></svg>
    <span>BRANDS OFFERS</span>
  </div>

  <footer class="abs footer">
    <div class="footer__col footer__col--left">
      <strong>PALEDORN PTY LTD</strong><br>P.O. Box 1200, Northvale<br>VIC 3000 Australia
    </div>
    <div class="footer__col footer__col--mid">
      <svg class="abs" style="left:24px;top:6px" width="28" height="28" viewBox="0 0 28 28"><circle cx="14" cy="14" r="12.5" fill="none" stroke="#fff" stroke-width="2"/><path d="M9 7 L12 7 L13 11 L11 12.5 Q12.5 16 15.5 17 L17 15 L21 16 L21 19 Q16 21 12 17 Q8 13 9 7 Z" fill="#fff"/></svg>
      <div style="padding-left:40px;text-align:left;margin-left:14px"><div class="ph-big">1-300-AEROLUX</div><div class="ph-big">+61 (3) 9000 1234</div></div>
      <div class="ph-small">24 HOURS A DAY 365 DAYS A YEAR</div>
    </div>
    <div class="footer__col footer__col--right">
      www.paledorn.com.au<br>info@paledorn.com.au<br>61 [0]3 9000 5678
    </div>
  </footer>
</section>

<section class="page page--back">
  <svg class="abs" style="left:0;top:0" width="536" height="170" viewBox="0 0 536 170">
    <defs>
      <linearGradient id="skyBack" x1="0" y1="0" x2="0" y2="1">
        <stop offset="0" stop-color="#6f95c4"/>
        <stop offset="1" stop-color="#d6e0ec"/>
      </linearGradient>
    </defs>
    <rect width="536" height="170" fill="url(#skyBack)" role="img" aria-label="Photo of an airliner climbing above the clouds"/>
    <path d="M0 98 Q240 200 536 92 L536 170 L0 170 Z" fill="var(--blue)"/>
    <path d="M0 120 Q250 200 536 102 L536 170 L0 170 Z" fill="#fff"/>
  </svg>

  <h1 class="abs title">OUR <b>AIRCRAFT</b></h1>
  <p class="abs intro">We welcome your enquiries about our private jet charter and FBO Services. Paledorn maintains an exclusive fleet of aircraft at our private hangers at Northvale and Eastmere Airports, Melbourne. Contact us anytime of the day or night, we never close!</p>

  <article class="abs card" style="top:274px">
    <div class="card__photo" role="img" aria-label="Photo of a business jet flying above the coast" style="background:linear-gradient(160deg,#4f79b8,#8fb0d8 60%,#5d7f9e)"></div>
    <svg class="abs" style="left:190px;top:80px" width="10" height="24" viewBox="0 0 10 24"><path d="M0 0 L10 12 L0 24 Z" fill="#6f93c4"/></svg>
    <div class="card__tab"><svg width="230" height="26" viewBox="0 0 230 26"><path d="M0 0 L230 0 L212 26 L18 26 Z" fill="#cdd8f0"/></svg><span>AEROLUX 35</span></div>
    <div class="spec" style="top:40px">
      <span class="spec__label" style="top:15px">DESCRIPTION</span>
      <span class="spec__value" style="top:0">APPOINTED LEATHER INTERIOR<br>DVD/CD ENTERTAINMENT SYSTEM<br>ENCLOSED LAVATORY<br>40 CUBIC FEET OF BAGGAGE AREA</span>
      <span class="spec__rule" style="top:56px"></span>
      <span class="spec__label" style="top:64px">SIZE</span><span class="spec__value" style="top:64px">8 PASSENGERS</span>
      <span class="spec__rule" style="top:78px"></span>
      <span class="spec__label" style="top:86px">WEIGHT</span><span class="spec__value" style="top:86px">24654524</span>
      <span class="spec__rule" style="top:100px"></span>
      <span class="spec__label" style="top:108px">RANGE</span><span class="spec__value" style="top:108px">3300 KM</span>
      <span class="spec__rule" style="top:122px"></span>
      <span class="spec__label" style="top:130px">SPEED</span><span class="spec__value" style="top:130px">820 KM/HR</span>
    </div>
  </article>

  <article class="abs card" style="top:464px">
    <div class="card__photo" role="img" aria-label="Photo of a business jet banking against a sunset sky" style="background:linear-gradient(170deg,#b9b3cc,#e8cdb0 55%,#9a8f86)"></div>
    <svg class="abs" style="left:190px;top:80px" width="10" height="24" viewBox="0 0 10 24"><path d="M0 0 L10 12 L0 24 Z" fill="#c9b4a6"/></svg>
    <div class="card__tab"><svg width="230" height="26" viewBox="0 0 230 26"><path d="M0 0 L230 0 L212 26 L18 26 Z" fill="#cdd8f0"/></svg><span>AEROLUX 35</span></div>
    <div class="spec" style="top:40px">
      <span class="spec__label" style="top:15px">DESCRIPTION</span>
      <span class="spec__value" style="top:0">APPOINTED LEATHER INTERIOR<br>DVD/CD ENTERTAINMENT SYSTEM<br>ENCLOSED LAVATORY<br>40 CUBIC FEET OF BAGGAGE AREA</span>
      <span class="spec__rule" style="top:56px"></span>
      <span class="spec__label" style="top:64px">SIZE</span><span class="spec__value" style="top:64px">8 PASSENGERS</span>
      <span class="spec__rule" style="top:78px"></span>
      <span class="spec__label" style="top:86px">WEIGHT</span><span class="spec__value" style="top:86px">24654524</span>
      <span class="spec__rule" style="top:100px"></span>
      <span class="spec__label" style="top:108px">RANGE</span><span class="spec__value" style="top:108px">3300 KM</span>
      <span class="spec__rule" style="top:122px"></span>
      <span class="spec__label" style="top:130px">SPEED</span><span class="spec__value" style="top:130px">820 KM/HR</span>
    </div>
  </article>

  <svg class="abs" style="left:0;top:650px" width="536" height="108" viewBox="0 0 536 108">
    <path d="M180 108 Q330 20 536 6 L536 20 Q340 34 200 108 Z" fill="var(--blue)"/>
  </svg>

  <div class="abs contact">
    <svg class="abs" style="left:0;top:0" width="40" height="40" viewBox="0 0 40 40"><circle cx="20" cy="20" r="18" fill="none" stroke="var(--blue)" stroke-width="2.4"/><path d="M13 10 L17 10 L18.5 16 L15.8 18 Q18 23 22.5 24.5 L24.5 22 L30 23.5 L30 27.5 Q23 30 17.5 24.5 Q12 19 13 10 Z" fill="var(--blue)"/></svg>
    <div class="contact__num">1-300-AEROLUX<br>+61 (3) 9000 1234</div>
    <div class="contact__hours">24 HOURS A DAY 365 DAYS A YEAR</div>
  </div>
  <div class="abs brand" style="left:372px;top:708px;font-size:24px"><span class="brand__dot" style="width:20px;height:20px"></span>PALEDORN</div>
</section>

</body>
</html>
```